New Book Cover for Website Advertising

I need a new book cover design to go on my website to generate pre-orders before my book is published. I have a previous design which I think needs a refresh. I want the new cover to complement the colours of my new website and logo. I'll attach the old book cover. All the words will remain the same, I just need an entirely new design

Target Market(s)

Corporate Leaders

Industry/Entity Type

Human resources

Font styles to use
Sans Serif

Colors
F0912C
F2A743
F7CA91
FBE8D2
FDF5EE
6B429C
8869AF
B7A5CE
E3DAEB
F3F0F8

Requirements
Must have
• A feeling of lightness, not dark
Should not have
• Any clip art or common stock photos

```html
<!DOCTYPE html>
<html lang="en">
<head>
<meta charset="UTF-8">
<title>The Steady Mentor – Book Cover</title>
<link href="https://fonts.googleapis.com/css2?family=Bebas+Neue&family=Raleway:ital,wght@0,300;0,400;1,400&display=swap" rel="stylesheet">
<style>
  :root {
    --backdrop: #e6e6e6;
    --cover-top: #faf1ea;
    --cover-bottom: #e7ded7;
    --spine-line: #efe6df;
    --ink: #111111;
    --accent: #ee8540;
    --accent-soft: #f7ca91;
    --paper: #f3efec;
  }
  * { margin: 0; padding: 0; box-sizing: border-box; }
  html, body {
    width: 1200px;
    height: 900px;
    overflow: hidden;
    background: var(--backdrop);
  }
  .book-cover {
    position: absolute;
    left: 380px;
    top: 121px;
    width: 440px;
    height: 658px;
    background: linear-gradient(160deg, var(--cover-top) 0%, #f5ebe4 50%, var(--cover-bottom) 100%);
  }
  .spine-edge {
    position: absolute;
    left: 22px;
    top: 0;
    bottom: 0;
    width: 3px;
    background: var(--spine-line);
  }
  .title-small {
    position: absolute;
    left: 77px;
    top: 60px;
    font-family: "Bebas Neue", sans-serif;
    font-size: 31px;
    line-height: 1;
    letter-spacing: 0.2em;
    color: var(--ink);
  }
  .title-main {
    position: absolute;
    left: 70px;
    font-family: "Bebas Neue", sans-serif;
    font-size: 88px;
    line-height: 1;
    letter-spacing: 0.21em;
  }
  .title-first { top: 92px; color: var(--ink); }
  .title-second { top: 183px; color: var(--accent); }
  .subtitle {
    position: absolute;
    left: 20px;
    right: 20px;
    top: 283px;
    font-family: "Raleway", sans-serif;
    font-style: italic;
    font-size: 14.5px;
    line-height: 18.5px;
    text-align: center;
    color: var(--ink);
  }
  .cover-illustration {
    position: absolute;
    left: 100px;
    top: 371px;
    width: 240px;
    height: 210px;
    background: linear-gradient(180deg, var(--paper) 0%, var(--accent-soft) 55%, var(--accent) 100%);
    border-radius: 4px;
  }
  .author {
    position: absolute;
    left: 0;
    right: 0;
    top: 604px;
    font-family: "Raleway", sans-serif;
    font-weight: 300;
    font-size: 34px;
    line-height: 1;
    letter-spacing: 0.22em;
    text-align: center;
    padding-left: 0.22em;
    color: var(--ink);
  }
</style>
</head>
<body>
  <main class="book-cover">
    <div class="spine-edge"></div>
    <h1>
      <span class="title-small">The</span>
      <span class="title-main title-first">Steady</span>
      <span class="title-main title-second">Mentor</span>
    </h1>
    <p class="subtitle">Explore How your Relational style shapes trust<br>with the people you guide and their energy,<br>growth and Output</p>
    <div class="cover-illustration" role="img" aria-label="Illustration of a businessman standing in an orange paper boat, looking through a telescope, with small clouds around"></div>
    <p class="author">MAREN HOLT</p>
  </main>
</body>
</html>
```